Business Card Velostra - Accounting firm

Hi my friend.
I'm coming back to you to see if it would be possible for you to make a modern and minimalist business card design.
In shades of blue like the great logo you offered me.
The ideal is a modern and aesthetic business card.
The goal is to give a professional effect to the first exchanges.
Renewal and innovation in the accounting world !!
I thank you !!
Good evening to you

Target Market(s)

Young, dynamic and sensitive to marketing

Industry/Entity Type

Finance And Accounting

Contact Information for Business Card

Company logo and name. Last name, First name, Phone number, email address, company address, website.

Font styles to use
Sans Serif

Requirements
Must have
• The ideal is a modern and aesthetic business card.

Mentions to include: Company logo and name. Last name, First name, Phone number, email address, company address, website.
Nice to have
• The goal is to give a professional effect to the first exchanges.
Should not have
• Simplistic or childish design

```html
<!DOCTYPE html>
<html lang="en">
<head>
<meta charset="UTF-8">
<title>Velostra Business Card</title>
<link rel="stylesheet" href="https://fonts.googleapis.com/css2?family=Poppins:wght@400;500;600;700&display=swap">
<style>
  :root {
    --navy: #1f2b60;
    --navy-text: #1c2459;
    --blue: #1f7fc9;
    --teal: #2bb3b8;
    --white: #ffffff;
    --backdrop: #e6e8ec;
    --card-shadow: 0 14px 36px rgba(20, 28, 60, 0.18);
  }
  * { box-sizing: border-box; margin: 0; padding: 0; }
  html, body {
    width: 1200px; height: 900px; overflow: hidden;
    background: var(--backdrop);
    font-family: "Poppins", sans-serif;
  }
  .canvas {
    width: 1200px; height: 900px;
    display: flex; flex-direction: column; align-items: center; justify-content: center;
    gap: 40px;
  }
  .card {
    position: relative;
    width: 700px; height: 400px;
    border-radius: 22px;
    overflow: hidden;
    box-shadow: var(--card-shadow);
  }
  /* Back side */
  .card-back { background: var(--navy); }
  .card-back .corner-bands { position: absolute; inset: 0; }
  .back-brand {
    position: absolute; left: 0; right: 0; top: 140px;
    display: flex; align-items: center; justify-content: center; gap: 16px;
  }
  .brand-dot { width: 34px; height: 34px; border-radius: 50%; background: var(--teal); }
  .brand-name { font-weight: 600; font-size: 64px; line-height: 1; letter-spacing: 0.5px; }
  .card-back .brand-name { color: var(--white); }
  .back-website {
    position: absolute; left: 0; right: 0; top: 268px;
    text-align: center; color: var(--white);
    font-size: 15px; font-weight: 500; letter-spacing: 2px;
  }
  /* Front side */
  .card-front { background: var(--white); display: flex; align-items: center; }
  .front-brand {
    width: 320px; display: flex; align-items: center; justify-content: center; gap: 12px;
  }
  .card-front .brand-name { color: var(--navy-text); font-size: 52px; }
  .card-front .brand-dot { width: 28px; height: 28px; }
  .divider { width: 2px; height: 210px; background: var(--blue); margin-right: 34px; }
  .contact { color: var(--navy-text); }
  .contact-name { font-weight: 700; font-size: 26px; line-height: 1.1; }
  .contact-role { color: var(--blue); font-size: 17px; font-weight: 500; margin-bottom: 12px; }
  .contact-list { list-style: none; }
  .contact-item {
    display: flex; align-items: flex-start; gap: 10px;
    font-size: 17px; line-height: 1.35; margin-bottom: 4px;
  }
  .contact-icon { width: 18px; height: 18px; flex: none; margin-top: 3px; }
</style>
</head>
<body>
<main class="canvas">

  <section class="card card-back" aria-label="Business card back">
    <svg class="corner-bands" viewBox="0 0 700 400" width="700" height="400" aria-hidden="true">
      <polygon points="175,0 310,0 0,100 0,58" fill="var(--white)"/>
      <polygon points="525,400 390,400 700,300 700,342" fill="var(--white)"/>
    </svg>
    <div class="back-brand">
      <span class="brand-dot"></span>
      <span class="brand-name">velostra</span>
    </div>
    <p class="back-website">WWW.VELOSTRA-FINANCE.COM</p>
  </section>

  <section class="card card-front" aria-label="Business card front">
    <div class="front-brand">
      <span class="brand-dot"></span>
      <span class="brand-name">velostra</span>
    </div>
    <div class="divider"></div>
    <div class="contact">
      <h1 class="contact-name">Marc Delorme</h1>
      <p class="contact-role">CEO/Founder</p>
      <ul class="contact-list">
        <li class="contact-item">
          <svg class="contact-icon" viewBox="0 0 24 24" aria-hidden="true"><path d="M6.6 10.8a15 15 0 0 0 6.6 6.6l2.2-2.2a1 1 0 0 1 1-.25 11.4 11.4 0 0 0 3.6.57 1 1 0 0 1 1 1V20a1 1 0 0 1-1 1A17 17 0 0 1 3 4a1 1 0 0 1 1-1h3.5a1 1 0 0 1 1 1c0 1.25.2 2.45.57 3.6a1 1 0 0 1-.25 1z" fill="var(--blue)"/></svg>
          <span>312-555-0148</span>
        </li>
        <li class="contact-item">
          <svg class="contact-icon" viewBox="0 0 24 24" aria-hidden="true"><rect x="2" y="5" width="20" height="14" rx="2" fill="none" stroke="var(--blue)" stroke-width="2"/><path d="M3 6l9 7 9-7" fill="none" stroke="var(--blue)" stroke-width="2"/></svg>
          <span>marc@velostra-finance.com</span>
        </li>
        <li class="contact-item">
          <svg class="contact-icon" viewBox="0 0 24 24" aria-hidden="true"><circle cx="12" cy="12" r="9.5" fill="none" stroke="var(--teal)" stroke-width="2"/><path d="M2.5 12h19M12 2.5c3 3 3 16 0 19M12 2.5c-3 3-3 16 0 19" fill="none" stroke="var(--teal)" stroke-width="1.6"/></svg>
          <span>www.velostra-finance.com</span>
        </li>
        <li class="contact-item">
          <svg class="contact-icon" viewBox="0 0 24 24" aria-hidden="true"><path d="M12 2a7 7 0 0 0-7 7c0 5 7 13 7 13s7-8 7-13a7 7 0 0 0-7-7z" fill="var(--teal)"/><circle cx="12" cy="9" r="2.6" fill="var(--white)"/></svg>
          <span>88 Harlow Street<br>Suite 210, Brookfield<br>OH 44021</span>
        </li>
      </ul>
    </div>
  </section>

</main>
</body>
</html>
```